Re-Brand of TindelMox along with a new website design

TindelMox Ltd are a software & database development company using technologies such as PHP, C#, HTML, JQuery, Flex, AS3, MySQL, Oracle, MSSQL. We like to target all types of business from small to large.

We are great at coding but rubbish at design so thats where we need your help!

We want a complete re-brand of TindelMox including logo, website design, and business cards.

We would like a design that is clean but other than that, please feel free to be creative.

****Logo****
We are looking for a logo that appears professional but with a splash of colour that indicates a creative side. Please see below some logos that we like the look of:

We like this one because it has a nice simple and clear font for the name of the company but also an icon which is colourful and stands out. http://markvault.example/2013/03/brivelo/

We like this one because it is very clean, simple and again very clear. http://markvault.example/2013/03/quantorels/

http://markvault.example/2013/03/tide-lamp/
http://markvault.example/2013/02/velmorin/
http://markvault.example/2013/01/art-gallery-tarnwick/

As you will see from all of these examples, the font is very clear but there is always a graphic representing the company too. This is what we like.

****Website****
These are some of the examples of websites we like:
https://www.zestrune.example/
https://www.chatterlane.example/home
http://www.haldenimagery.example/
http://www.vistor.example/
http://quillbay.example/
https://www.usebriefnest.example/personal-intros
http://www.marmotpanel.example/

The current site can be found at tindelmox.example.uk

Reason: We have extended the deadline of the project by 5 days as I realise the original deadline was very tight.

Software

Requirements
Must have
• Website must have the following pages
Home
Services
Projects
About Us
Contact Us

```html
<!DOCTYPE html>
<html lang="en">
<head>
<meta charset="utf-8">
<title>TindelMox — web, software, IT services</title>
<link href="https://fonts.googleapis.com/css2?family=Questrial&family=Raleway:wght@200&display=swap" rel="stylesheet">
<style>
  :root {
    --page-grey: #dedede;
    --hero-top: #2effb0;
    --hero-bottom: #3cf2cb;
    --ink: #2f2f2f;
    --ink-soft: #3a3a3a;
    --white: #ffffff;
    --rule: #c8c8c8;
    --footer-bg: #fbfbfb;
  }
  * { margin: 0; padding: 0; box-sizing: border-box; }
  html, body {
    width: 1200px;
    height: 1066px;
    overflow: hidden;
    background: var(--page-grey);
    font-family: "Questrial", "Helvetica Neue", Arial, sans-serif;
    color: var(--ink);
  }
  .site {
    position: relative;
    width: 1200px;
    height: 1066px;
  }
  .top-band {
    height: 156px;
    background: var(--page-grey);
  }
  .hero {
    position: relative;
    height: 570px;
    background: linear-gradient(180deg, var(--hero-top) 0%, var(--hero-top) 45%, var(--hero-bottom) 100%);
    text-align: center;
  }
  .contact-badge {
    position: absolute;
    top: 72px;
    right: 76px;
    width: 164px;
    height: 164px;
    border-radius: 50%;
    background: var(--white);
    border: 2px dashed var(--rule);
    box-shadow: 0 0 0 1px #e8e8e8;
    display: flex;
    align-items: center;
    justify-content: center;
    font-size: 12px;
    letter-spacing: 0.5px;
    color: var(--ink);
    text-decoration: none;
  }
  .brand {
    position: absolute;
    top: 96px;
    left: 0;
    width: 100%;
    font-size: 112px;
    line-height: 1;
    letter-spacing: -3px;
    color: var(--ink-soft);
  }
  .services-nav {
    position: absolute;
    top: 366px;
    left: 0;
    width: 100%;
    font-size: 16px;
    color: var(--ink);
  }
  .services-nav .divider {
    display: inline-block;
    width: 3px;
    height: 12px;
    background: var(--ink);
    margin: 0 16px;
    vertical-align: -1px;
  }
  .intro {
    position: absolute;
    top: 424px;
    left: 50%;
    width: 360px;
    transform: translateX(-50%);
    font-size: 11.5px;
    line-height: 1.32;
    color: var(--ink);
  }
  .intro p + p { margin-top: 12px; }
  .call-to-action {
    height: 80px;
    padding-top: 8px;
    text-align: center;
    font-size: 11.5px;
    font-weight: bold;
    letter-spacing: 0.3px;
  }
  .projects-bar {
    position: absolute;
    left: 0;
    bottom: 0;
    width: 100%;
    height: 260px;
    background: var(--footer-bg);
    border-top: 2px dashed var(--rule);
    text-align: center;
  }
  .projects-bar h2 {
    font-family: "Raleway", "Helvetica Neue", Arial, sans-serif;
    font-weight: 200;
    font-size: 62px;
    line-height: 1;
    padding-top: 14px;
    color: var(--ink);
  }
</style>
</head>
<body>
<div class="site">
  <header class="top-band"></header>
  <section class="hero">
    <a class="contact-badge" href="#contact">contact us</a>
    <h1 class="brand">TindelMox</h1>
    <nav class="services-nav">
      <span>web</span><span class="divider"></span><span>sofware</span><span class="divider"></span><span>IT services</span>
    </nav>
    <div class="intro">
      <p>Based in Ipswich our clients are both local and national; large and small. You may be a start-up business in need of a ‘get me up and running quickly’ website, or a multi-million pound brand looking for an all singing, all dancing be-spoke app.</p>
      <p>Maybe you are experiencing the pains and pleasures of growing your business and it’s time to improve your brand-ing and to trade in your current home-spun website for something more professional.</p>
    </div>
  </section>
  <p class="call-to-action">Let’s chat today about where we can take your business.</p>
  <section class="projects-bar">
    <h2>projects</h2>
  </section>
</div>
</body>
</html>
```